Tallbrook Meridian Advisory needs business cards

Tallbrook Meridian Advisory is a new approach to consulting: we believe in partnering our clients in a hands-on, side-by-side, rolling-up-our sleeves approach, rather than being removed and aloof consultants.

We have a logo design developped through PixelHarbor (see attachment) and need to move to the stage of designing a business card for our 7 founding members.

Target Market(s)

Senior executives in local and global companies (such as Fizzmont Tonic, Hollanby, Brevard, etc)

Industry/Entity Type

Business

Requirements
Must have
• Look and feel: The design reflect the logo: i.e. professional, modern and approachable (as opposed to corporate traditional and remote). We are looking for a high quality, premium design.

Content must haves:
- prominent: our logo, person's name, function, phone number and e-mail address
- less prominent: company address and website

Example: Tallbrook Meridian Advisory logo, Mireille Vostag, Partner, +44 (0)781 209 3375, mireille_vostag@tallbrookmeridian.example / 17 Pelham Crescent, Wrenford, Kentmere, UK, WF4 7QX - www.tallbrookmeridian.example

- Both sides of the card can be used
- Both versions of the logo can be used (on black or on white)

```html
<!DOCTYPE html>
<html lang="en">
<head>
<meta charset="utf-8">
<title>Tallbrook Meridian Advisory – Business Card</title>
<link rel="stylesheet" href="https://fonts.googleapis.com/css2?family=Carlito:wght@400;700&display=swap">
<style>
  :root {
    --stage: #000000;
    --sky-top: #74c4ef;
    --sky-bottom: #1690c8;
    --card-white: #ffffff;
    --ink: #111111;
    --mark-blue: #4fb6d8;
    --frame-line: rgba(255, 255, 255, 0.75);
    --band-top: #6cc0ee;
    --band-bottom: #1a8cc6;
  }
  * { margin: 0; padding: 0; box-sizing: border-box; }
  html, body {
    width: 1060px;
    height: 1200px;
    overflow: hidden;
    background: var(--stage);
    font-family: "Carlito", "Calibri", sans-serif;
    color: var(--ink);
  }
  .canvas { position: relative; width: 1060px; height: 1200px; }

  /* Front side */
  .card-front {
    position: absolute;
    left: 85px; top: 79px;
    width: 882px; height: 508px;
    background: linear-gradient(to bottom, var(--sky-top), var(--sky-bottom));
  }
  .logo-frame {
    position: absolute;
    left: 173px; top: 137px;
    width: 540px; height: 236px;
    border: 1px solid var(--frame-line);
    border-radius: 30px;
  }
  .logo-plate {
    position: absolute;
    left: 196px; top: 159px;
    width: 495px; height: 192px;
    background: var(--card-white);
    border-radius: 22px;
  }

  /* Shared brand lockup */
  .brand {
    position: absolute;
    display: flex;
    align-items: center;
  }
  .brand-dot {
    border-radius: 50%;
    background: var(--mark-blue);
    flex: none;
  }
  .brand-name {
    font-weight: 400;
    color: var(--ink);
    line-height: 1.02;
    white-space: nowrap;
  }
  .card-front .brand { left: 52px; top: 34px; gap: 24px; }
  .card-front .brand-dot { width: 124px; height: 124px; }
  .card-front .brand-name { font-size: 34px; }

  /* Back side */
  .card-back {
    position: absolute;
    left: 83px; top: 613px;
    width: 882px; height: 508px;
    background: var(--card-white);
    overflow: hidden;
  }
  .holder { position: absolute; left: 54px; top: 70px; font-size: 24px; line-height: 34px; }
  .holder-name { font-weight: 700; }
  .phone { position: absolute; right: 62px; top: 73px; font-size: 24px; }

  .card-back .brand { left: 222px; top: 202px; gap: 28px; }
  .card-back .brand-dot { width: 134px; height: 134px; }
  .card-back .brand-name { font-size: 38px; }

  .address {
    position: absolute;
    left: 385px; top: 336px;
    font-size: 22px;
    line-height: 33px;
    font-style: normal;
    white-space: nowrap;
  }
  .card-band {
    position: absolute;
    left: 0; bottom: 0;
    width: 100%; height: 60px;
    background: linear-gradient(to bottom, var(--band-top), var(--band-bottom));
  }
</style>
</head>
<body>
<main class="canvas">
  <section class="card-front" aria-label="Card front">
    <div class="logo-frame"></div>
    <div class="logo-plate">
      <div class="brand">
        <span class="brand-dot"></span>
        <span class="brand-name">Tallbrook Meridian<br>Advisory</span>
      </div>
    </div>
  </section>

  <section class="card-back" aria-label="Card back">
    <div class="holder">
      <p class="holder-name">Mireille Vostag</p>
      <p class="holder-role">Partner</p>
    </div>
    <p class="phone">+44 (0)781 209 3375</p>

    <div class="brand">
      <span class="brand-dot"></span>
      <span class="brand-name">Tallbrook Meridian<br>Advisory</span>
    </div>

    <address class="address">
      17 Pelham Crescent, Wrenford, Kentmere,<br>
      mireille_vostag@tallbrookmeridian.example<br>
      UK, WF4 7QX - www.tallbrookmeridian.example
    </address>

    <div class="card-band"></div>
  </section>
</main>
</body>
</html>
```